Larchmere Hockey Academy

We are are Ice Hockey Development Company that provided on-ice Hockey development services. We need a Landing Page with tabs to direct to individual program pages.
Landing Page
About Page
Winter Program Page
Spring Program Page
Summer Program Page
Team Page
Tournament Page

```html
<!DOCTYPE html>
<html lang="en">
<head>
<meta charset="utf-8">
<title>Larchmere Hockey Academy</title>
<link href="https://fonts.googleapis.com/css2?family=Hind:wght@400;500;600;700&display=swap" rel="stylesheet">
<style>
  :root {
    --ink: #000000;
    --paper: #ffffff;
    --green: #006400;
    --green-bright: #2e9a2e;
    --ice-light: #f4f4f6;
    --ice-mid: #dedde2;
  }
  * { box-sizing: border-box; margin: 0; padding: 0; }
  html, body { width: 1200px; height: 853px; overflow: hidden; }
  body {
    position: relative;
    background: var(--paper);
    color: var(--ink);
    font-family: "Hind", sans-serif;
  }
  .site-header {
    position: absolute; left: 69px; top: 28px; width: 1079px; height: 68px;
    border-bottom: 2px solid var(--ink);
  }
  .brand {
    position: absolute; left: 0; top: 2px;
    font-weight: 700; font-size: 17px; line-height: 18px; letter-spacing: 0.5px;
    color: var(--ink); text-transform: uppercase;
  }
  .main-nav {
    position: absolute; right: 6px; top: 35px;
    display: flex; gap: 28px;
    font-size: 13px; font-weight: 400; letter-spacing: 0.2px;
  }
  .main-nav a { color: var(--ink); text-decoration: none; }
  .hero-photo {
    position: absolute; left: 69px; top: 126px; width: 676px; height: 491px;
    background: radial-gradient(ellipse at 55% 55%, var(--ice-light) 0%, var(--ice-mid) 100%);
  }
  .hero-copy { position: absolute; left: 768px; top: 202px; width: 370px; }
  .hero-title {
    font-size: 53px; font-weight: 700; line-height: 1; letter-spacing: 0.5px;
  }
  .hero-text {
    margin-top: 26px; font-size: 11.3px; line-height: 18.3px; width: 362px;
  }
  .btn {
    display: inline-flex; align-items: center; justify-content: center;
    margin-top: 23px; width: 125px; height: 42px;
    background: var(--green); color: var(--paper);
    font-size: 11px; text-decoration: none; letter-spacing: 0.2px;
  }
  .site-footer {
    position: absolute; left: 0; top: 681px; width: 1200px; height: 172px;
    background: var(--ink); color: var(--paper);
  }
  .footer-brand {
    position: absolute; left: 69px; top: 38px; width: 123px; height: 72px;
    background: var(--paper); border-radius: 10px;
    display: flex; align-items: center; justify-content: center; text-align: center;
    color: var(--ink); font-weight: 700; font-size: 12px; line-height: 13px;
  }
  .footer-col { position: absolute; top: 50px; font-size: 11px; line-height: 16.7px; }
  .footer-col h3 { font-size: 11px; font-weight: 600; color: var(--green-bright); }
  .footer-col a { display: block; color: var(--paper); text-decoration: none; }
  .col-who { left: 363px; }
  .col-programs { left: 497px; }
  .col-contact { left: 610px; }
  .social { position: absolute; top: 38px; left: 1067px; display: flex; gap: 26px; }
  .social span { width: 25px; height: 25px; border-radius: 5px; background: var(--paper); display: block; }
  .copyright {
    position: absolute; top: 140px; left: 0; width: 1220px; text-align: center;
    font-size: 11px; font-weight: 600;
  }
</style>
</head>
<body>
  <header class="site-header">
    <div class="brand">Larchmere<br>Hockey<br>Academy</div>
    <nav class="main-nav">
      <a href="#">ABOUT</a>
      <a href="#">TEAM</a>
      <a href="#">WINTER PROGRAM</a>
      <a href="#">SPRING PROGRAM</a>
      <a href="#">SUMMER PROGRAM</a>
      <a href="#">TOURNAMENTS</a>
    </nav>
  </header>

  <div class="hero-photo" role="img" aria-label="Youth hockey player in a white and green jersey taking a shot on the ice"></div>

  <section class="hero-copy">
    <h1 class="hero-title">LOREM IPSOM</h1>
    <p class="hero-text">Lorem ipsum dolor sit amet, consectetur adipiscing elit, sed do eiusmod tempor incididunt ut labore et dolore magna aliqua. Sed vulputate mi sit amet mauris. Quisque sagittis purus sit amet volutpat consequat mauris nunc. Sed felis eget velit aliquet sagittis id. Nisl pretium fusce id velit ut tortor pretium. Sed vulputate mi sit amet mauris commodo quis imperdiet. Cursus sit amet dictum sit amet justo donec enim diam. Scelerisque eu ultrices vitae auctor eu augue ut lectus. Nibh tortor id aliquet lectus proin nibh nisl condimentum. Arcu cursus vitae congue mauris rhoncus aenean vel elit scelerisque. Cursus mattis molestie a iaculis.</p>
    <a class="btn" href="#">LEARN MORE</a>
  </section>

  <footer class="site-footer">
    <div class="footer-brand">LARCHMERE<br>HOCKEY<br>ACADEMY</div>
    <div class="footer-col col-who">
      <h3>WHO WE ARE</h3>
      <a href="#">ABOUT</a>
      <a href="#">TEAM</a>
      <a href="#">TOURNAMENTS</a>
    </div>
    <div class="footer-col col-programs">
      <h3>PROGRAMS</h3>
      <a href="#">WINTER</a>
      <a href="#">SPRING</a>
      <a href="#">SUMMER</a>
    </div>
    <div class="footer-col col-contact">
      <h3>CONTACT US</h3>
    </div>
    <div class="social" aria-label="Social links">
      <span></span>
      <span></span>
    </div>
    <p class="copyright">COPYRIGHT 2023</p>
  </footer>
</body>
</html>
```